Law Firm Needs Brochure Redesign Using New Logo

We are a personal injury law firm that does auto injuries and other personal injury cases. We want a new brochure that has our updated logo and information. Instead of gold and black, we want more navy, as matches the new logo. The Auto Liability portion should read: "(required by the state of Arizona in the amounts of $25,000 per person / $50,000 per accident, but a higher amount may be best )." The other information can remain the same. We'd like the brochure to keep the same professional tone as the previous brochure.
Our website is https://www.brandtlegalpartners.example/.

```html
<!DOCTYPE html>
<html lang="en">
<head>
<meta charset="utf-8">
<title>Brandt Legal Partners – Auto Accident Brochure</title>
<link rel="stylesheet" href="https://fonts.googleapis.com/css2?family=Raleway:wght@300;400;500;600;700&display=swap">
<style>
:root{
  --navy:#152a4f;
  --navy-deep:#0f1f3c;
  --gold:#c4933a;
  --sky:#8fb8dc;
  --white:#ffffff;
  --paper:#e8e8ea;
  --ink:#2a2f3a;
}
*{box-sizing:border-box;margin:0;padding:0}
html,body{width:1200px;height:459px;overflow:hidden}
body{background:var(--paper);font-family:"Raleway",sans-serif;color:var(--white);position:relative}
.spread{position:absolute;top:20px;width:545px;height:420px;display:grid;grid-template-columns:repeat(3,1fr);box-shadow:0 6px 14px rgba(0,0,0,.18)}
.spread--outside{left:30px}
.spread--inside{left:625px}
.panel{position:relative;display:flex;flex-direction:column;overflow:hidden}

/* outside, panel 1 */
.stat{text-align:center;display:flex;flex-direction:column;justify-content:center;align-items:center}
.stat--gold{background:var(--gold);height:85px}
.stat--navy{background:var(--navy);height:74px}
.stat__over{font-size:7.5px;font-weight:400;letter-spacing:.2px}
.stat__num{font-size:26px;font-weight:300;line-height:1}
.stat--navy .stat__num{color:var(--gold);font-size:26px}
.stat__note{font-size:5.6px;font-weight:400;line-height:1.35;margin-top:3px;padding:0 20px}
.photo{position:relative}
.photo--drivers{height:125px;background:linear-gradient(120deg,#7a8fa3,#c9a58e 45%,#dbe3ef)}
.notch{position:absolute;width:0;height:0;border-left:15px solid transparent;border-right:15px solid transparent}
.notch--sky-down{top:0;left:20px;border-top:26px solid var(--sky)}
.brandbox{background:var(--white);display:flex;align-items:center;justify-content:center;gap:6px}
.brandbox--p1{height:52px}
.brand{display:flex;align-items:center;gap:6px}
.brand__dot{width:18px;height:18px;border-radius:50%;background:var(--navy);flex:none}
.brand__name{color:var(--navy);font-weight:700;font-size:9.5px;letter-spacing:1.2px;line-height:1.15;text-transform:uppercase}
.promise{background:var(--navy);flex:1;font-size:5.8px;line-height:1.45;text-align:center;padding:10px 22px;display:flex;align-items:center}

/* outside, panel 2 */
.panel--contact{background:var(--white);color:var(--ink)}
.contact__brand{margin-top:auto;padding:0 14px 8px 28px;border-bottom:1px solid var(--gold);margin-right:14px}
.contact__brand .brand__dot{width:14px;height:14px}
.contact__brand .brand__name{font-size:7.5px}
.contact__list{list-style:none;padding:9px 10px 12px 16px;font-size:6.3px;line-height:1.35}
.contact__list li{display:flex;gap:6px;align-items:flex-start;margin-bottom:6px}
.contact__list svg{width:8px;height:8px;flex:none;margin-top:1px}

/* outside, panel 3 */
.panel--cover{background:var(--navy-deep)}
.cover__head{height:88px;padding:13px 12px 0 16px}
.cover__title{font-size:11.5px;font-weight:400;line-height:1.15}
.cover__title em{font-style:normal;color:var(--gold);font-weight:600}
.cover__lede{font-size:5.6px;line-height:1.35;margin-top:8px;width:60px}
.photo--car{height:249px;background:radial-gradient(ellipse at 70% 50%,#5a5d63 0%,#25272c 45%,#0c0d10 80%)}
.brandbox--p3{height:53px;justify-content:flex-start;padding-left:16px}
.brandbox--p3 .brand__dot{width:22px;height:22px}
.brandbox--p3 .brand__name{font-size:10.5px}
.goldbar{height:6px;background:var(--gold)}
.cover__url{flex:1;background:var(--navy);display:flex;align-items:center;justify-content:center;font-size:6.4px;font-weight:700;color:var(--gold)}

/* inside, panel 1 */
.panel--tips{background:var(--navy);padding:12px 0 6px}
.section-title{font-size:11.5px;font-weight:600;padding:0 12px;margin-bottom:5px}
.tips{list-style:none;flex:1;display:flex;flex-direction:column}
.tips li{font-size:5.9px;line-height:1.5;padding:5px 12px;border-top:1px solid rgba(196,147,58,.55);flex:1;display:flex;align-items:center}
.tips li:first-child{border-top:none}
.tips b{color:var(--gold);font-weight:600}

/* inside, panel 2 */
.coverage{background:var(--gold);height:210px;padding:12px 12px 0 12px}
.coverage .section-title{color:var(--navy);padding:0;margin-bottom:6px}
.coverage p{font-size:5.8px;line-height:1.3;margin-bottom:6px;font-weight:400}
.coverage b{font-weight:700}
.photo--shield{flex:1;background:linear-gradient(160deg,#cfd9e6,#6f8fb8 40%,#2d4f80)}
.notch--gold-down{top:0;left:18px;border-top:24px solid var(--gold)}
.notch--navy-down{top:0;left:18px;border-top:24px solid var(--navy)}
.notch--gold-up{bottom:0;right:18px;border-bottom:24px solid var(--gold)}

/* inside, panel 3 */
.photo--belt{height:210px;background:linear-gradient(150deg,#3a2226,#6b3b43 35%,#8a939e 65%,#2e3542)}
.behavior{background:var(--white);color:var(--ink);height:155px;padding:14px 12px 0}
.behavior h3{font-size:11px;font-weight:600;color:var(--navy-deep);margin-bottom:6px}
.behavior p{font-size:5.9px;line-height:1.55;margin-bottom:7px}
.behavior .accent{color:var(--gold);font-weight:600}
.behavior p.accent{line-height:1.3}
.photo--phone{flex:1;background:linear-gradient(120deg,#1b2b48,#3f5478 60%,#22314d)}
</style>
</head>
<body>

<section class="spread spread--outside">
  <div class="panel panel--stats">
    <div class="stat stat--gold">
      <span class="stat__over">OVER</span>
      <span class="stat__num">107,000</span>
      <span class="stat__note">crashes will happen in the state of Arizona this year</span>
    </div>
    <div class="photo photo--drivers" role="img" aria-label="Photo of a startled driver and passenger inside a car">
      <span class="notch notch--sky-down"></span>
    </div>
    <div class="stat stat--navy">
      <span class="stat__over">OVER</span>
      <span class="stat__num">700</span>
      <span class="stat__note">of them will result in fatalities.</span>
    </div>
    <div class="brandbox brandbox--p1">
      <div class="brand"><span class="brand__dot"></span><span class="brand__name">Brandt Legal<br>Partners</span></div>
    </div>
    <p class="promise">If we don't win, you don't pay attorney fees. That seems fair to us. Know what's happening with your case, get the answers to your questions and work on getting better with the confidence that you've got an excellent group of people working for you.</p>
  </div>

  <div class="panel panel--contact">
    <div class="contact__brand">
      <div class="brand"><span class="brand__dot"></span><span class="brand__name">Brandt Legal<br>Partners</span></div>
    </div>
    <ul class="contact__list">
      <li><svg viewBox="0 0 10 10"><path d="M5 .6a3.3 3.3 0 0 0-3.3 3.3C1.7 6.4 5 9.6 5 9.6s3.3-3.2 3.3-5.7A3.3 3.3 0 0 0 5 .6zm0 4.6a1.3 1.3 0 1 1 0-2.6 1.3 1.3 0 0 1 0 2.6z" fill="#c4933a"/></svg><span>4410 N. Cedar Ridge Drive Suite B110<br>Phoenix AZ 85031</span></li>
      <li><svg viewBox="0 0 10 10"><circle cx="5" cy="5" r="4.3" fill="none" stroke="#c4933a" stroke-width=".9"/><path d="M3.4 3c.2-.3.5-.3.7 0l.5.7c.1.2 0 .4-.1.5l-.3.3c.3.6.8 1.1 1.4 1.4l.3-.3c.1-.1.3-.2.5-.1l.7.5c.3.2.3.5 0 .7-.4.4-1 .5-1.5.2C4.7 6.4 3.6 5.3 3.1 4.3c-.2-.5-.1-1 .3-1.3z" fill="#c4933a"/></svg><span>602.555.0147</span></li>
      <li><svg viewBox="0 0 10 10"><rect x=".8" y="2.2" width="8.4" height="5.8" rx=".6" fill="none" stroke="#c4933a" stroke-width=".9"/><path d="M1 2.6 5 5.6l4-3" fill="none" stroke="#c4933a" stroke-width=".9"/></svg><span>info@brandtlegalpartners.example<br>www.brandtlegalpartners.example</span></li>
    </ul>
  </div>

  <div class="panel panel--cover">
    <header class="cover__head">
      <h1 class="cover__title"><em>Protect</em> your <em>family</em><br>in case of a car accident</h1>
      <p class="cover__lede">A little knowledge and preparation go a long way</p>
    </header>
    <div class="photo photo--car" role="img" aria-label="Photo of a dark luxury car headlight in low light"></div>
    <div class="brandbox brandbox--p3">
      <div class="brand"><span class="brand__dot"></span><span class="brand__name">Brandt Legal<br>Partners</span></div>
    </div>
    <div class="goldbar"></div>
    <p class="cover__url">www.brandtlegalpartners.example</p>
  </div>
</section>

<section class="spread spread--inside">
  <div class="panel panel--tips">
    <h2 class="section-title">Top 10 Tips to Avoid a Crash</h2>
    <ul class="tips">
      <li><span><b>Anyone making a left turn must wait for all oncoming traffic to clear before proceeding.</b> Yes, even if the light has turned yellow. Wait to be sure that all traffic has stopped.</span></li>
      <li><span><b>When your light turns green,</b> check to be sure that no vehicles are entering the intersection late.</span></li>
      <li><span><b>Allow plenty of room between you and the car in front of you.</b> Traffic can stop in an instant, even if you can't see anything ahead.</span></li>
      <li><span><b>Avoid being distracted.</b> Teenagers are especially susceptible to losing focus if there are too many friends in the car.</span></li>
      <li><span><b>Keep the volume of your radio down and never wear headphones.</b> Cars are very soundproof these days, but you need to be able to hear an ambulance or police siren.</span></li>
      <li><span><b>Be especially careful on the weekends and early morning hours.</b></span></li>
      <li><span><b>Don't speed.</b> Speed is a factor in most crashes. Street lights are timed and the freeway has traffic. It's likely you won't get there much faster even if you do speed.</span></li>
      <li><span><b>Don't drink and drive.</b> Many cab companies offer a free service to get you home safe.</span></li>
      <li><span><b>Use your turn signals.</b> This gives an early warning to vehicles you may not be able to see.</span></li>
    </ul>
  </div>

  <div class="panel panel--coverage">
    <div class="coverage">
      <h2 class="section-title">Have the Right Coverage</h2>
      <p>Many people don't know about the different kinds of insurance available. In addition to health insurance, we suggest:</p>
      <p><b>Auto Liability</b> (required by the state of Arizona in the amounts of $25,000 per person / $50,000 per accident, but a higher amount may be best).</p>
      <p><b>Uninsured or Underinsured Motorist Coverage.</b> This protects YOU when the other driver doesn't have insurance or not enough.</p>
      <p><b>Medical Payments Coverage.</b> Up to $5,000 in coverage will be paid out to you no matter who is at fault in an accident and does not need to be reimbursed.</p>
      <p><b>Homeowners / Renters Insurance.</b> Protects you in case of injuries on your property as well as damage to your home from covered events.</p>
    </div>
    <div class="photo photo--shield" role="img" aria-label="Photo of a hand touching a car insurance shield icon">
      <span class="notch notch--navy-down" style="border-top-color:var(--gold)"></span>
    </div>
  </div>

  <div class="panel panel--behavior">
    <div class="photo photo--belt" role="img" aria-label="Photo of a hand fastening a seatbelt">
      <span class="notch notch--gold-up"></span>
    </div>
    <div class="behavior">
      <h3>Model Safe Behavior</h3>
      <p><span class="accent">Always buckle up.</span> Always put your children in car seats/boosters that are rated for their height and weight.</p>
      <h3>Never Text While Driving</h3>
      <p>Studies have shown that texting while driving is as dangerous as driving intoxicated.</p>
      <p class="accent">Show your children that no text is more important than your safety. It can wait.</p>
    </div>
    <div class="photo photo--phone" role="img" aria-label="Photo of a driver holding a phone at the wheel">
      <span class="notch notch--gold-down"></span>
    </div>
  </div>
</section>

</body>
</html>
```